Hip Surgeon needs a web page re-design.

I have a web page to provide information about the diseases of the hip joint for the patients from my private practice since 2008. I need a re-design job for a fresh new look.
We have made a new logo and a new stationery design here in Marqueloft (please see the uploaded files) and I want to make my web page look-alike the new design concepts.
I like the color blue and tones of blue, matching my logo and stationery.
I don't like "busy" designs. It must be clean, elegant and ease to read. The final design should be "mobile friendly" if possible.
Please visit my website www.vilacorendasul.com.br to take a look and get some inspiration.

```html
<!DOCTYPE html>
<html lang="en">
<head>
<meta charset="utf-8">
<title>Dr. Rafael M. Quintela – Cirurgia do Quadril</title>
<link href="https://fonts.googleapis.com/css2?family=Ubuntu:wght@300;400;500;700&display=swap" rel="stylesheet">
<style>
:root{
  --blue:#1b6fc4;
  --blue-mid:#3d8bd6;
  --blue-light:#5aa3e2;
  --ink:#4a4a4a;
  --white:#fff;
}
*{box-sizing:border-box;margin:0;padding:0}
html,body{width:1150px;height:1200px;overflow:hidden;background:var(--white);font-family:"Ubuntu",sans-serif;color:var(--ink)}
.page{position:relative;width:1150px;height:1200px}
.hero{position:absolute;left:0;top:0;width:1150px;height:545px;background:linear-gradient(180deg,#6fa8da 0%,#4f8fca 40%,#3f79b4 75%,#5e8fbf 100%)}
.xray{position:absolute;left:0;top:121px;width:1150px;height:424px;background:radial-gradient(ellipse at 30% 40%,rgba(210,230,248,.35),transparent 60%),radial-gradient(ellipse at 80% 55%,rgba(200,225,245,.3),transparent 55%)}
.topbar{position:absolute;right:12px;top:6px;color:var(--white);font-size:13px;font-weight:500;letter-spacing:.2px}
.topbar span{margin-left:14px}
.navband{position:absolute;left:362px;top:32px;width:788px;height:89px;background:rgba(27,111,196,.85)}
.nav{position:absolute;left:48px;top:33px;display:flex;gap:31px;list-style:none}
.nav li{color:var(--white);font-weight:500;font-size:15px;letter-spacing:.3px}
.brand{position:absolute;left:0;top:28px;width:362px;height:95px;background:var(--white);display:flex;align-items:center;padding-left:10px;gap:10px}
.brand-mark{flex:none;width:70px;height:70px;border-radius:50%;border:8px solid var(--blue)}
.brand-name{color:var(--blue);font-weight:400;font-size:26px;line-height:1.15;white-space:nowrap}
.brand-name small{display:block;font-size:20px}
.hero-title{position:absolute;left:130px;top:334px;color:var(--white);font-size:57px;font-weight:300;line-height:1;text-shadow:0 2px 6px rgba(0,0,0,.3)}
.hero-title strong{display:block;font-weight:700}
.profile{position:absolute;left:690px;top:285px;width:396px;height:184px;background:rgba(61,139,214,.92);color:var(--white);padding:42px 16px 0}
.profile h2{font-size:21px;font-weight:500;margin-bottom:6px}
.profile p{font-size:14px;font-weight:300;line-height:1.18;letter-spacing:.3px}
.profile p+p{margin-top:14px}
.profile a{color:var(--white)}
.portrait{position:absolute;left:703px;top:185px;width:135px;height:135px;border-radius:50%;background:linear-gradient(160deg,#e9e1d4,#c9b7a3 60%,#f2f2f2);border:3px solid #dbe8f5}
.services{position:absolute;left:0;top:545px;width:1150px;height:361px;background:linear-gradient(180deg,#ffffff 0%,#e4eef8 40%,#9fc4e8 100%)}
.divider{position:absolute;top:0;width:3px;height:361px;background:var(--blue-mid)}
.service{position:absolute;top:56px;width:256px}
.service h3{font-size:17px;font-weight:500;color:#3a3a3a;margin-bottom:10px;white-space:nowrap}
.service .thumb{width:252px;height:81px;background:linear-gradient(90deg,#777,#bbb 50%,#666)}
.service p{margin-top:14px;height:106px;font-size:13px;font-weight:300;line-height:1.17;letter-spacing:.5px;color:#555}
.btn{display:block;margin-top:6px;width:124px;height:36px;line-height:36px;text-align:center;background:var(--white);border-radius:2px;font-size:14px;font-weight:300;color:#444}
.promos{position:absolute;left:18px;top:924px;display:flex;gap:18px}
.promo{position:relative;width:359px;height:184px;background:var(--blue-mid);color:var(--white);overflow:hidden}
.cover{position:absolute;left:12px;top:20px;width:105px;height:162px;background:linear-gradient(180deg,#f5f5f5,#d9d3c6)}
.promo-text{position:absolute;left:139px;top:10px;width:200px}
.promo-text h4{font-size:24px;font-weight:400;line-height:1}
.promo-text h5{font-size:18px;font-weight:400;line-height:1.02;margin-bottom:6px}
.promo-text p{font-size:13px;font-weight:300;line-height:1.28;letter-spacing:.4px}
.screen{position:absolute;left:16px;top:32px;width:184px;height:124px;background:linear-gradient(180deg,#f3f3f3,#d4dbe3)}
.channel-name{position:absolute;left:243px;top:56px;width:62px;height:58px;background:#d9302a;color:var(--white);font-size:15px;font-weight:500;display:flex;align-items:center;justify-content:center;border-radius:6px}
.channel-link{position:absolute;left:220px;top:128px;font-size:16px;font-weight:500;text-decoration:underline}
.phone-ring{position:absolute;left:37px;top:20px;width:81px;height:81px;border-radius:50%;border:5px solid var(--white);background:var(--blue)}
.book{position:absolute;left:40px;top:120px;font-size:24px;font-weight:500;line-height:1.15}
.agent{position:absolute;right:0;top:0;width:146px;height:184px;background:linear-gradient(180deg,#c9a27a,#e8d2bd 40%,#2a2a2a 80%)}
.footer{position:absolute;left:0;top:1136px;width:1150px;border-top:1px solid var(--blue-mid)}
.footer-nav{position:absolute;left:18px;top:14px;display:flex;gap:14px;list-style:none}
.footer-nav li{color:var(--blue-mid);font-size:15px;font-weight:500}
.copy{position:absolute;left:18px;top:41px;font-size:12px;font-weight:300;letter-spacing:.4px;color:#555}
.footer-brand{position:absolute;right:18px;top:16px;display:flex;align-items:center;gap:6px;color:var(--blue);font-size:15px;line-height:1.1}
.footer-brand .dot{width:34px;height:34px;border-radius:50%;border:4px solid var(--blue)}
</style>
</head>
<body>
<div class="page">
  <header class="hero">
    <div class="xray" role="img" aria-label="X-ray of a pelvis with hip prostheses"></div>
    <div class="topbar"><span>Email:dr.rafael@vilacorendasul.com.br</span><span>Call: 41 35550180 or 41 35550181</span></div>
    <div class="navband">
      <ul class="nav"><li>SAIBA MAIS</li><li>CURRICULUM LATTES</li><li>LINKS</li><li>DOWNLOADS</li><li>ATUALIDADES</li><li>CONTATO</li></ul>
    </div>
    <div class="brand"><div class="brand-mark"></div><div class="brand-name">Dr. Rafael M. Quintela<small>Cirurgia do Quadril</small></div></div>
    <h1 class="hero-title">Surgery of the<strong>HipJoint</strong></h1>
    <section class="profile">
      <h2>Dr. Rafael Moreira Quintela</h2>
      <p>Welcome to the site "Vila Corenda Hip"!</p>
      <p>The purpose of this site is to provide the lay public information on major diseases and surgical procedures involving the hip and pelvis, as prosthetic hip arthroscopy (surgery video), etc. <a href="#">read more</a></p>
    </section>
    <div class="portrait" role="img" aria-label="Portrait photo of the surgeon"></div>
  </header>

  <section class="services">
    <span class="divider" style="left:292px"></span>
    <span class="divider" style="left:570px"></span>
    <span class="divider" style="left:849px"></span>
    <article class="service" style="left:31px"><h3>Non Operative Treatment</h3><div class="thumb" role="img" aria-label="Doctor holding a stethoscope" style="background:linear-gradient(90deg,#e7d5c8,#b2887a 50%,#f0e8e4)"></div><p>The artificial hip operation is one of the options that you have in trying to control the pain of a damaged hip. It is not a life saving operation and hence every patient should carefully consider...</p><span class="btn">Read more</span></article>
    <article class="service" style="left:309px"><h3>Primary Hip Replacement</h3><div class="thumb" role="img" aria-label="X-ray of a primary hip replacement"></div><p>A hip replacement operation is one of the most successful operations in Orthopaedic Surgery. Hundreds of thousands of these operations are now carried out every year worldwide with excellent results...</p><span class="btn">Read more</span></article>
    <article class="service" style="left:587px"><h3>Hip Resurfacing</h3><div class="thumb" role="img" aria-label="X-ray of a hip resurfacing implant"></div><p>The concept of hip resurfacing as opposed to replacing the joint has been attractive to hip surgeons for a long time. The first attempts at doing so were carried out many years before the advent...</p><span class="btn">Read more</span></article>
    <article class="service" style="left:866px"><h3>Revision Hip Replacement</h3><div class="thumb" role="img" aria-label="X-ray of a revision hip replacement" style="background:linear-gradient(90deg,#333,#888 50%,#333)"></div><p>In spite of the generally good results after total hip replacement, there are times when things do go wrong. This fortunately, happens much less frequently now than was the case...</p><span class="btn">Read more</span></article>
  </section>

  <section class="promos">
    <div class="promo"><div class="cover" role="img" aria-label="Cover of the hip prosthesis care manual"></div><div class="promo-text"><h4>Download</h4><h5>Manual: Prosthetic hip: care after your surgery.</h5><p>Click on the cover below to download free from the Second Edition of the manual: "Hip Prosthesis - care after your surgery"</p></div></div>
    <div class="promo"><div class="screen" role="img" aria-label="Screenshot of the video channel page"></div><div class="channel-name">Vidora</div><span class="channel-link">See Our Channel</span></div>
    <div class="promo"><div class="phone-ring"><svg width="71" height="71" viewBox="0 0 71 71"><path d="M20 34c0-8 7-12 15.5-12S51 26 51 34h-7v-4h-17v4z" fill="#fff"/><rect x="24" y="33" width="23" height="14" rx="2" fill="#fff"/><circle cx="35.5" cy="40" r="3.5" fill="#1b6fc4"/></svg></div><div class="book">Agende Sua<br>Consulta</div><div class="agent" role="img" aria-label="Receptionist wearing a headset"></div></div>
  </section>

  <footer class="footer">
    <ul class="footer-nav"><li>SAIBA MAIS</li><li>CURRICULUM LATTES</li><li>LINKS</li><li>DOWNLOADS</li><li>ATUALIDADES</li><li>CONTATO</li></ul>
    <p class="copy">Copyright (c)2013 by vilacorendasul.com.br | Privacy policy</p>
    <div class="footer-brand"><span class="dot"></span><span>Dr. Rafael M. Quintela<br>Cirurgia do Quadril</span></div>
  </footer>
</div>
</body>
</html>
```